Post it Note design

POST-IT NOTE DESIGN (CONTENT)
Size recommended: 4x6 for handwriting space.
Header (Bold):
Lighting Issue Detected on Your Property
Sub-header:
During our routine night inspection, we noted the following item(s):
Checkbox List:
⬜ Building Lights Out
⬜ Pole Lights Out
⬜ Sign Not Illuminated
⬜ Other ________________________
Action Line:
We can provide a quote or dispatch service right away.
Area for notes
Contact Block (Bold & Centered):
Brightwell Fixture Care Inc.
Service@BrightwellFixtureCare.com
www.BrightwellFixtureCare.com
877-514-6082
Industry/Entity Type
Electrical lighting
Colors
Designer to choose colors to be used in the design.
Look and feel
Each slider illustrates characteristics of the customer's brand and the style your logo design should communicate.

```html
<!DOCTYPE html>
<html lang="en">
<head>
<meta charset="utf-8">
<title>Brightwell Fixture Care Inc. – Lighting Issue Notice</title>
<link rel="stylesheet" href="https://fonts.googleapis.com/css2?family=Poppins:wght@400;500;700&display=swap">
<style>
  :root {
    --page-bg: #e3e3e3;
    --paper: #ffffff;
    --alert-red: #d41f30;
    --navy: #2b3a8c;
    --ink-navy: #27337f;
    --ink-grey: #4a4442;
    --hazard-yellow: #f4d21c;
    --hazard-dark: #1e1e1e;
  }
  html, body {
    margin: 0;
    padding: 0;
    width: 1200px;
    height: 2665px;
    overflow: hidden;
    background: var(--page-bg);
    font-family: "Poppins", sans-serif;
  }
  .notice-card {
    position: absolute;
    left: 100px;
    top: 580px;
    width: 1000px;
    height: 1504px;
    background: var(--paper);
    box-shadow: 0 6px 24px rgba(0,0,0,0.08);
    overflow: hidden;
  }
  .brand {
    height: 314px;
    display: flex;
    align-items: center;
    justify-content: center;
    text-align: center;
  }
  .brand-name {
    margin: 0;
    font-weight: 700;
    font-size: 56px;
    line-height: 66px;
    color: var(--ink-navy);
    text-transform: uppercase;
    letter-spacing: 1px;
  }
  .alert-band {
    height: 403px;
    background: var(--alert-red);
    box-sizing: border-box;
    padding: 47px 0 0 83px;
  }
  .alert-title {
    margin: 0;
    color: #fff;
    font-weight: 700;
    font-size: 100px;
    line-height: 100px;
    letter-spacing: -2px;
    text-transform: uppercase;
  }
  .checklist {
    position: relative;
    height: 447px;
  }
  .checklist-intro {
    position: absolute;
    left: 79px;
    top: 38px;
    margin: 0;
    font-weight: 400;
    font-size: 36px;
    line-height: 50px;
    color: var(--ink-grey);
    text-transform: uppercase;
  }
  .check-item {
    position: absolute;
    left: 77px;
    display: flex;
    align-items: center;
    font-size: 40px;
    color: var(--ink-navy);
    height: 50px;
  }
  .check-box {
    width: 36px;
    height: 36px;
    background: var(--alert-red);
    border: 1.5px solid var(--ink-navy);
    box-sizing: border-box;
    margin-right: 52px;
  }
  .item-building { top: 167px; }
  .item-pole { top: 230px; }
  .item-sign { top: 295px; }
  .item-other { top: 360px; }
  .write-line {
    display: inline-block;
    width: 332px;
    height: 30px;
    border-bottom: 2px solid var(--ink-navy);
    margin-left: 14px;
  }
  .contact-panel {
    position: relative;
    height: 340px;
    background: var(--navy);
    color: #fff;
  }
  .panel-texture {
    position: absolute;
    inset: 0 0 24px 0;
    background: radial-gradient(circle at 65% 55%, rgba(255,255,255,0.06), rgba(255,255,255,0) 45%);
  }
  .action-line {
    position: absolute;
    left: 79px;
    top: 48px;
    margin: 0;
    font-size: 25px;
    font-weight: 500;
    text-transform: uppercase;
    letter-spacing: 0.3px;
  }
  .contact-row {
    position: absolute;
    left: 79px;
    display: flex;
    align-items: center;
    font-size: 24px;
    height: 36px;
  }
  .row-email { top: 113px; }
  .row-web { top: 168px; }
  .row-phone { top: 225px; }
  .contact-icon {
    width: 36px;
    height: 36px;
    margin-right: 17px;
    flex: none;
  }
  .hazard-band {
    position: absolute;
    left: 0;
    right: 0;
    bottom: 0;
    height: 24px;
    background: linear-gradient(180deg, var(--hazard-yellow), #e7c414);
  }
</style>
</head>
<body>
  <main class="notice-card">
    <header class="brand">
      <p class="brand-name">Brightwell Fixture<br>Care Inc.</p>
    </header>

    <section class="alert-band">
      <h1 class="alert-title">Lighting Issue<br>Detected On<br>Your Property.</h1>
    </section>

    <section class="checklist">
      <p class="checklist-intro">During our routine night inspection,<br>we noted the following item:</p>
      <div class="check-item item-building"><span class="check-box"></span>Building Lights Out</div>
      <div class="check-item item-pole"><span class="check-box"></span>Pole Lights Out</div>
      <div class="check-item item-sign"><span class="check-box"></span>Sign Not Illuminated</div>
      <div class="check-item item-other"><span class="check-box"></span>Other<span class="write-line"></span></div>
    </section>

    <footer class="contact-panel">
      <div class="panel-texture" role="img" aria-label="Faint photo of a light fixture behind the contact details"></div>
      <p class="action-line">We can provide a quote or dispatch service right away.</p>

      <div class="contact-row row-email">
        <svg class="contact-icon" viewBox="0 0 36 36" aria-hidden="true">
          <circle cx="18" cy="18" r="18" fill="#d41f30"/>
          <rect x="9.5" y="12" width="17" height="12" rx="1" fill="none" stroke="#fff" stroke-width="2"/>
          <path d="M10 13 L18 19.5 L26 13" fill="none" stroke="#fff" stroke-width="2"/>
        </svg>
        <span>Service@BrightwellFixtureCare.com</span>
      </div>

      <div class="contact-row row-web">
        <svg class="contact-icon" viewBox="0 0 36 36" aria-hidden="true">
          <circle cx="18" cy="18" r="18" fill="#d41f30"/>
          <rect x="9" y="15" width="11" height="6" rx="3" transform="rotate(-45 14.5 18)" fill="none" stroke="#fff" stroke-width="2"/>
          <rect x="16" y="15" width="11" height="6" rx="3" transform="rotate(-45 21.5 18)" fill="none" stroke="#fff" stroke-width="2"/>
        </svg>
        <span>brightwellfixturecare.com</span>
      </div>

      <div class="contact-row row-phone">
        <svg class="contact-icon" viewBox="0 0 36 36" aria-hidden="true">
          <circle cx="18" cy="18" r="18" fill="#d41f30"/>
          <path d="M12.5 10.5 l3 0 l1.5 4 l-2 1.5 c1 2.5 2.5 4 5 5 l1.5 -2 l4 1.5 l0 3 c0 1 -1 2 -2 2 c-7 -0.5 -12.5 -6 -13 -13 c0 -1 1 -2 2 -2 z" fill="#fff"/>
        </svg>
        <span>877-514-6082</span>
      </div>

      <div class="hazard-band" role="img" aria-label="Yellow and black hazard stripe band"></div>
    </footer>
  </main>
</body>
</html>
```